Create a PPTX template for our business

We need a Powerpoint and Keynote template design for a new company called "Borvelon" We connect hotel guests to hotel employees through text messaging so guests can ask for what they need during their stay. The name "Borvelon" is derived from the word "Affinity" which is how we want our hotel customer's employees and their guests to feel about each other. The color palette chosen is meant to evoke feelings of "warmth" and "comfort," which is how most people feel when they have a strong affinity to each other. The "-ium" ending of Borvelon is intended to give a technological feel to our business since we use technology to connect people together.

A *.ai file is included which contains our logo.

Hotel

```html
<!DOCTYPE html>
<html lang="en">
<head>
<meta charset="utf-8">
<title>Borvelon – Presentation Template</title>
<link rel="stylesheet" href="https://fonts.googleapis.com/css2?family=PT+Sans:ital,wght@0,400;0,700;1,400&family=PT+Sans+Narrow:wght@400;700&display=swap">
<style>
  :root {
    --backdrop: #1c2222;
    --charcoal-top: #3a3a3a;
    --charcoal-bottom: #8a8a8a;
    --paper: #f4f4f4;
    --paper-edge: #e2e2e2;
    --lime: #d9dd2c;
    --lime-dark: #a9ad12;
    --teal: #1e9a97;
    --teal-dark: #0f6f6d;
    --teal-ink: #16706c;
    --ink: #3b3b3b;
    --white: #ffffff;
    --subtle: #d8d8d8;
  }
  * { box-sizing: border-box; margin: 0; padding: 0; }
  html, body { width: 818px; height: 1200px; overflow: hidden; }
  body {
    background: var(--backdrop);
    font-family: "PT Sans", Arial, sans-serif;
    position: relative;
  }
  .slide {
    position: absolute;
    left: 33px;
    width: 754px;
    overflow: hidden;
    box-shadow: 0 4px 14px rgba(0,0,0,.6);
    background: linear-gradient(180deg, var(--white) 0%, var(--paper) 60%, var(--paper-edge) 100%);
  }
  .slide--cover { top: 22px; height: 568px; }
  .slide--content { top: 602px; height: 566px; }

  /* cover */
  .cover-header {
    position: absolute; left: 0; top: 0; width: 100%; height: 332px;
    background: linear-gradient(180deg, var(--charcoal-top) 0%, var(--charcoal-bottom) 100%);
    border-bottom: 5px solid var(--lime);
  }
  .cover-title {
    position: absolute; right: 44px; top: 124px;
    font-family: "PT Sans Narrow", Arial, sans-serif;
    font-weight: 700; font-size: 42px; color: var(--white);
    text-align: right;
  }
  .cover-subtext {
    position: absolute; right: 44px; top: 182px; width: 460px;
    font-family: "PT Sans Narrow", Arial, sans-serif;
    font-size: 16.5px; line-height: 25px; color: var(--subtle);
    text-align: right;
  }
  .portrait {
    position: absolute; left: 21px; top: 198px;
    width: 274px; height: 274px; border-radius: 50%;
    background: var(--lime);
    padding: 7px;
  }
  .portrait__ring {
    width: 100%; height: 100%; border-radius: 50%;
    background: var(--white); padding: 4px;
    border: 4px solid var(--teal);
  }
  .portrait__photo {
    width: 100%; height: 100%; border-radius: 50%;
    background: radial-gradient(circle at 50% 40%, #c8937a 0%, #a8826e 30%, #ece9e6 55%, #2f2f36 85%);
  }
  .brand {
    position: absolute; left: 420px; top: 404px;
    display: flex; align-items: center; gap: 14px;
  }
  .brand__dot { width: 30px; height: 30px; border-radius: 50%; background: var(--teal); }
  .brand__name {
    font-family: "PT Sans", Arial, sans-serif;
    font-size: 44px; font-weight: 400; color: #555; letter-spacing: 1px;
  }

  /* footer bar */
  .footer {
    position: absolute; left: 0; bottom: 0; width: 100%; height: 56px;
    background: linear-gradient(180deg, var(--teal) 0%, var(--teal-dark) 100%);
    border-top: 4px solid var(--lime);
  }
  .slide-number {
    position: absolute; left: 20px; top: 9px; width: 38px; height: 34px;
    background: linear-gradient(180deg, var(--lime) 0%, var(--lime-dark) 100%);
    color: var(--white); font-size: 20px; text-align: center; line-height: 34px;
    border-radius: 2px;
  }
  .footer__text {
    position: absolute; left: 117px; top: 14px;
    font-style: italic; font-size: 17px; color: var(--white);
  }
  .footer__text--tagline { left: 80px; font-size: 16px; }
  .nav-button {
    position: absolute; top: 8px; height: 36px;
    background: linear-gradient(180deg, #e6e93a 0%, var(--lime-dark) 100%);
    color: var(--white); font-size: 15px; line-height: 36px; text-align: center;
  }
  .nav-button--forward { clip-path: polygon(0 0, 82% 0, 100% 50%, 82% 100%, 0 100%); padding-right: 8px; }
  .nav-button--back { clip-path: polygon(18% 0, 100% 0, 100% 100%, 18% 100%, 0 50%); padding-left: 8px; }

  /* content slide */
  .slide-flag { position: absolute; left: 0; top: 17px; }
  .slide-title {
    position: absolute; left: 35px; top: 14px;
    font-family: "PT Sans Narrow", Arial, sans-serif;
    font-weight: 700; font-size: 31px; color: var(--teal-ink);
  }
  .section-heading {
    position: absolute; left: 55px; top: 92px;
    font-family: "PT Sans Narrow", Arial, sans-serif;
    font-weight: 700; font-size: 21px; color: var(--teal-dark);
  }
  .checklist {
    position: absolute; left: 55px; top: 130px; width: 620px;
    list-style: none;
  }
  .checklist li {
    position: relative; padding-left: 28px;
    font-family: "PT Sans Narrow", Arial, sans-serif;
    font-size: 16px; line-height: 24.6px; color: var(--ink);
  }
  .checklist svg { position: absolute; left: 0; top: 3px; }
</style>
</head>
<body>
<svg width="0" height="0" style="position:absolute">
  <symbol id="tick-box" viewBox="0 0 20 18">
    <rect x="1" y="4" width="13" height="13" fill="none" stroke="#16706c" stroke-width="1.6"/>
    <path d="M4 10 L8 14 L18 1" fill="none" stroke="#16706c" stroke-width="3" stroke-linecap="round" stroke-linejoin="round"/>
  </symbol>
</svg>

<section class="slide slide--cover">
  <div class="cover-header">
    <h1 class="cover-title">Project Title Here</h1>
    <p class="cover-subtext">Subtext here Subtext here Subtext here Subtext here Subtext here Subtext here Subtext here Subtext here</p>
  </div>
  <div class="portrait">
    <div class="portrait__ring">
      <div class="portrait__photo" role="img" aria-label="Portrait photo of the presenter"></div>
    </div>
  </div>
  <div class="brand">
    <span class="brand__dot"></span>
    <span class="brand__name">BORVELON</span>
  </div>
  <footer class="footer">
    <div class="slide-number">01</div>
    <span class="footer__text">01/02/15</span>
    <div class="nav-button nav-button--forward" style="left:675px;width:62px;">Start</div>
  </footer>
</section>

<section class="slide slide--content">
  <svg class="slide-flag" width="28" height="38" viewBox="0 0 28 38">
    <polygon points="0,0 28,0 28,38 0,38 12,19" fill="#1e9a97"/>
  </svg>
  <h2 class="slide-title">Slide Title Presentation</h2>
  <h3 class="section-heading">Calder Modern Real Estate</h3>
  <ul class="checklist">
    <li><svg width="20" height="18"><use href="#tick-box"/></svg>High volume local boutique real estate company</li>
    <li><svg width="20" height="18"><use href="#tick-box"/></svg>Specialize in selling homes throughout the San Francisco Bay Area</li>
    <li><svg width="20" height="18"><use href="#tick-box"/></svg>Focus on modern marketing techniques and thinking outside the box</li>
    <li><svg width="20" height="18"><use href="#tick-box"/></svg>“High Tech and High Touch” approach to real estate</li>
    <li><svg width="20" height="18"><use href="#tick-box"/></svg>Certified Green Business Everything is done and stored online. No File Cabinets in our offices!</li>
    <li><svg width="20" height="18"><use href="#tick-box"/></svg>Exceptional web presence far beyond other local real estate companies</li>
    <li><svg width="20" height="18"><use href="#tick-box"/></svg>Clean, streamline, and hip marketing materials</li>
    <li><svg width="20" height="18"><use href="#tick-box"/></svg>A company constantly looking into the latest real estate trends, tools, and technology to better assist their agents and clients sell homes in the modern world, all while embracing tried and true real estate values and practices as well</li>
    <li><svg width="20" height="18"><use href="#tick-box"/></svg>Leading authority for architectural homes and recognized world wide</li>
    <li><svg width="20" height="18"><use href="#tick-box"/></svg>Not Just Modern Homes! We focus on Modern Real Estate<br>Practices through and through.</li>
  </ul>
  <footer class="footer">
    <div class="slide-number">04</div>
    <span class="footer__text footer__text--tagline">Tagline/Slogan about Your Company</span>
    <div class="nav-button nav-button--back" style="left:600px;width:62px;">Back</div>
    <div class="nav-button nav-button--forward" style="left:674px;width:62px;">Next</div>
  </footer>
</section>
</body>
</html>
```